Rising Side by Side A Handbook to Help Managers and Crews Climb to Fresh Peaks of Results

We need a book cover design for a book titled: Rising Side by Side:
A Handbook to Help Managers and Crews Climb to Fresh Peaks of Results
The book is intended to enhance the author's personal brand and promote the author's consulting services. The book also teaches: How To Help Leaders and Teams Reach New Heights of Performance. I would like to use the colors from the www.bramblewickadvisory.example website (blue and orange). The design should communicate credibility and expertise in the topic of the book.

Target Market(s)

Municipal and Industrial and Energy Industry Team Leaders and Teams

Industry/Entity Type

water and waste water, energy, power generation, petrochmical

Requirements
Must have
• Look like a Kestrel Ledger best seller. Look professional and appealling
Nice to have
• Sell at the airport. Executives keep in their office.
Should not have
• Do not plagiarize.

```html
<!DOCTYPE html>
<html lang="en">
<head>
<meta charset="utf-8">
<title>Rising Side by Side – Book Cover</title>
<link rel="stylesheet" href="https://fonts.googleapis.com/css2?family=Saira+Extra+Condensed:wght@800&family=Montserrat:wght@700;800&display=swap">
<style>
  :root {
    --page-bg: #e9e6e1;
    --navy: #0f1d33;
    --navy-deep: #0a1526;
    --orange: #f0a13c;
    --orange-deep: #d9782a;
    --orange-light: #f7b955;
    --sky-violet: #8a7fa8;
    --sky-rose: #d9a6b8;
    --sky-glow: #f6e2c4;
    --white: #ffffff;
  }
  * { margin: 0; padding: 0; box-sizing: border-box; }
  html, body {
    width: 1200px; height: 1200px; overflow: hidden;
    background: var(--page-bg);
  }
  .book-cover {
    position: absolute;
    left: 250px; top: 60px;
    width: 700px; height: 1080px;
    background: var(--navy);
    overflow: hidden;
    box-shadow: 0 18px 40px rgba(0,0,0,0.25);
  }
  .cover-scene {
    position: absolute; left: 0; top: 0;
    width: 100%; height: 600px;
    background:
      radial-gradient(ellipse 45% 30% at 52% 38%, var(--sky-glow) 0%, rgba(246,226,196,0) 70%),
      linear-gradient(180deg, var(--sky-violet) 0%, var(--sky-rose) 28%, #b58a86 42%, #3a3443 58%, var(--navy) 100%);
  }
  .cover-title {
    position: absolute; left: 40px; top: 400px;
    width: 620px; height: 360px;
  }
  .cover-title svg { display: block; width: 620px; height: 360px; }
  .title-text {
    font-family: "Saira Extra Condensed", "Arial Narrow", sans-serif;
    font-weight: 800;
  }
  .title-rule {
    position: absolute; left: 120px; top: 782px;
    width: 460px; height: 2px;
    background: linear-gradient(90deg, rgba(255,255,255,0) 0%, rgba(255,255,255,0.85) 50%, rgba(255,255,255,0) 100%);
  }
  .cover-subtitle {
    position: absolute; left: 20px; right: 20px; top: 805px;
    text-align: center;
    font-family: "Montserrat", Arial, sans-serif;
    font-weight: 700;
    font-size: 25px;
    line-height: 1.4;
    white-space: nowrap;
    color: var(--white);
  }
  .cover-subtitle .accent { color: var(--orange); }
  .author-band {
    position: absolute; left: 0; bottom: 0;
    width: 100%; height: 130px;
    background: linear-gradient(180deg, var(--orange-light) 0%, var(--orange) 50%, var(--orange-deep) 100%);
    display: flex; align-items: center; justify-content: center;
  }
  .author-name {
    font-family: "Montserrat", Arial, sans-serif;
    font-weight: 800;
    font-size: 40px;
    letter-spacing: 1px;
    color: var(--navy-deep);
    text-transform: uppercase;
  }
</style>
</head>
<body>
  <main class="book-cover">
    <div class="cover-scene" role="img" aria-label="Silhouetted team helping each other climb a mountain peak against a sunrise sky"></div>

    <h1 class="cover-title" aria-label="Rising Side by Side">
      <svg viewBox="0 0 620 360" aria-hidden="true">
        <defs>
          <linearGradient id="title-fill" x1="0" y1="0" x2="0" y2="1">
            <stop offset="0" stop-color="#f7b955"/>
            <stop offset="0.55" stop-color="#f0a13c"/>
            <stop offset="1" stop-color="#d9782a"/>
          </linearGradient>
        </defs>
        <text class="title-text" x="0" y="200" font-size="230" textLength="620" lengthAdjust="spacingAndGlyphs" fill="url(#title-fill)">RISING</text>
        <text class="title-text" x="0" y="350" font-size="150" textLength="620" lengthAdjust="spacingAndGlyphs" fill="url(#title-fill)">SIDE BY SIDE</text>
      </svg>
    </h1>

    <div class="title-rule"></div>

    <p class="cover-subtitle">
      A Handbook to Help <span class="accent">Managers and Crews</span><br>
      <span class="accent">Climb to Fresh Peaks</span> of Results
    </p>

    <footer class="author-band">
      <span class="author-name">Author Name</span>
    </footer>
  </main>
</body>
</html>
```